6 - 8 'Holistic' Instagram Graphics

Hi there!
We are looking to build up a library of Graphic Templates to use as Instagram & Facebook posts for our Holistic Medi Spa (& 3 other companies eventually)
This competition is for a sample of 6 - 8 designs. For the winner(s), we will make an agreement for a batch order (Looking for 200+ designs in total), and will be looking to make a long term arrangement.
Please find a full job description in the attached Word Document.
Any questions, don't hesitate to ask.
Thanks!
Medical Spa

```html
<!DOCTYPE html>
<html lang="en">
<head>
<meta charset="utf-8">
<title>Holistic Spa Post Templates</title>
<link href="https://fonts.googleapis.com/css2?family=Great+Vibes&family=Outfit:wght@300;700&family=Bodoni+Moda:wght@700&display=swap" rel="stylesheet">
<style>
  :root {
    --page-bg: #f2f2f2;
    --frame: #ffffff;
    --teal: #2bb3b1;
    --teal-deep: #17807e;
    --teal-text: #16a58f;
    --teal-light: #66d6c9;
    --mint: #e7f7f3;
    --skin: #ecd9cc;
    --skin-shadow: #cdb3a3;
    --towel: #f6f4f2;
    --ink: #1c1c1c;
    --author: #1f6b55;
    --white: #ffffff;
  }
  * { margin: 0; padding: 0; box-sizing: border-box; }
  html, body { width: 1200px; height: 848px; overflow: hidden; }
  body { background: var(--page-bg); position: relative; }

  .post-set {
    position: absolute;
    top: 243px;
    left: 27px;
    display: flex;
    gap: 30px;
  }
  .post-frame {
    width: 362px;
    height: 362px;
    padding: 16px;
    background: var(--frame);
  }
  .post {
    position: relative;
    width: 330px;
    height: 330px;
    overflow: hidden;
  }

  /* Decorative ornament placeholders (soft discs in ornament tones) */
  .ornament {
    position: absolute;
    border-radius: 50%;
  }
  .ornament--white {
    background: radial-gradient(circle, rgba(255,255,255,0.42) 0%, rgba(255,255,255,0.22) 55%, rgba(255,255,255,0) 72%);
  }
  .ornament--teal {
    background: radial-gradient(circle, rgba(32,150,150,0.85) 0%, rgba(32,150,150,0.5) 50%, rgba(32,150,150,0) 72%);
  }

  /* Post 1 — Smile, breathe */
  .post--breathe { background: var(--teal); }
  .breathe__hands {
    position: absolute; left: 0; top: 0; width: 220px; height: 190px;
    background:
      radial-gradient(ellipse at 30% 55%, rgba(230,220,210,0.55) 0%, rgba(230,220,210,0) 45%),
      linear-gradient(135deg, var(--teal-deep) 0%, rgba(43,179,177,0) 85%);
  }
  .breathe__ornament--left { left: -45px; top: 150px; width: 230px; height: 230px; }
  .breathe__ornament--right { right: -40px; top: 130px; width: 170px; height: 170px; }
  .breathe__hexagon { position: absolute; left: 0; top: 0; }
  .script {
    position: absolute;
    font-family: 'Great Vibes', cursive;
    font-weight: 400;
    color: var(--white);
    line-height: 0.95;
  }
  .breathe__headline { left: 32px; top: 14px; font-size: 33px; }
  .breathe__headline span { display: block; }
  .breathe__headline span + span { margin-left: -14px; font-size: 28px; }
  .breathe__closing { right: 8px; bottom: 12px; font-size: 28px; text-align: right; }

  /* Post 2 — Quote */
  .post--quote {
    background:
      radial-gradient(ellipse at 18% 85%, rgba(70,120,45,0.9) 0%, rgba(70,120,45,0) 45%),
      linear-gradient(165deg, #3e3a22 0%, #6e5d34 35%, #8a7c3e 55%, #5b7a34 78%, #3a6526 100%);
  }
  .quote__flowers {
    position: absolute; right: -10px; bottom: -10px; width: 250px; height: 150px;
    background:
      radial-gradient(ellipse at 70% 65%, #ee7fae 0%, #dc5f95 28%, rgba(220,95,149,0.55) 52%, rgba(220,95,149,0) 75%),
      radial-gradient(ellipse at 20% 80%, rgba(240,140,180,0.7) 0%, rgba(240,140,180,0) 45%);
  }
  .quote__ornament--left { left: -40px; top: -40px; width: 105px; height: 105px; }
  .quote__ornament--right { right: -40px; top: -40px; width: 105px; height: 105px; }
  .quote__shield { position: absolute; left: 0; top: 0; }
  .quote__text {
    position: absolute; left: 0; top: 14px; width: 330px;
    font-family: 'Outfit', sans-serif; font-weight: 300;
    font-size: 27.5px; line-height: 35px; color: var(--ink);
    text-align: center;
  }
  .quote__author {
    position: absolute; left: 0; top: 207px; width: 330px;
    font-family: 'Outfit', sans-serif; font-weight: 700;
    font-size: 11px; letter-spacing: 1.5px; color: var(--author);
    text-align: center;
  }

  /* Post 3 — Keep calm */
  .post--calm { background: var(--mint); }
  .calm__photo {
    position: absolute; left: 0; top: 0; width: 164px; height: 330px;
    background:
      radial-gradient(ellipse at 50% 55%, var(--skin) 0%, rgba(236,217,204,0) 55%),
      radial-gradient(ellipse at 20% 35%, var(--towel) 0%, rgba(246,244,242,0) 45%),
      linear-gradient(165deg, #f0ebe7 0%, #e9ddd4 50%, var(--skin-shadow) 100%);
  }
  .calm__ornament--top { left: 105px; top: -55px; width: 130px; height: 130px; }
  .calm__ornament--bottom { left: 85px; bottom: -55px; width: 140px; height: 140px; }
  .calm__headline {
    position: absolute; left: 181px; top: 58px;
    font-family: 'Bodoni Moda', serif; font-weight: 700;
    font-size: 44px; line-height: 51px; letter-spacing: -0.5px;
  }
  .calm__headline span { display: block; }
  .calm__headline .dark { color: var(--teal-text); }
  .calm__headline .light { color: var(--teal-light); }
</style>
</head>
<body>
  <main class="post-set">

    <div class="post-frame">
      <section class="post post--breathe">
        <div class="breathe__hands" role="img" aria-label="Photo of a therapist's gloved hands holding a facial device"></div>
        <div class="ornament ornament--white breathe__ornament--left" role="img" aria-label="Faint white mandala ornament"></div>
        <div class="ornament ornament--white breathe__ornament--right" role="img" aria-label="Faint white mandala ornament"></div>
        <svg class="breathe__hexagon" width="330" height="330" viewBox="0 0 330 330">
          <defs>
            <radialGradient id="treatment-photo" cx="55%" cy="55%" r="65%">
              <stop offset="0%" stop-color="#ecd6c6"/>
              <stop offset="45%" stop-color="#e6d8cf"/>
              <stop offset="100%" stop-color="#f3f1ee"/>
            </radialGradient>
          </defs>
          <polygon points="165,21 289,93 289,235 165,307 41,235 41,93" fill="#ffffff" fill-opacity="0.35"/>
          <polygon points="165,39 273,101.5 273,226.5 165,289 57,226.5 57,101.5" fill="url(#treatment-photo)" role="img" aria-label="Photo of a woman receiving a facial treatment"/>
        </svg>
        <h2 class="script breathe__headline"><span>Smile,</span><span>breathe...</span></h2>
        <p class="script breathe__closing">and go<br>slowly</p>
      </section>
    </div>

    <div class="post-frame">
      <section class="post post--quote">
        <div class="quote__flowers" role="img" aria-label="Garden photo with pink blossoms"></div>
        <div class="ornament ornament--teal quote__ornament--left" role="img" aria-label="Teal mandala ornament"></div>
        <div class="ornament ornament--teal quote__ornament--right" role="img" aria-label="Teal mandala ornament"></div>
        <svg class="quote__shield" width="330" height="330" viewBox="0 0 330 330">
          <polygon points="12,0 316,0 316,160 167,246 12,160" fill="#ffffff" fill-opacity="0.7"/>
        </svg>
        <blockquote class="quote__text">The natural<br>healing within<br>each of us is the<br>greatest force in<br>getting well.</blockquote>
        <p class="quote__author">ELIAS THORNE</p>
      </section>
    </div>

    <div class="post-frame">
      <section class="post post--calm">
        <div class="calm__photo" role="img" aria-label="Photo of a relaxed woman receiving a facial treatment"></div>
        <div class="ornament ornament--white calm__ornament--top" role="img" aria-label="White mandala ornament"></div>
        <div class="ornament ornament--white calm__ornament--bottom" role="img" aria-label="White mandala ornament"></div>
        <h2 class="calm__headline">
          <span class="dark">Keep</span>
          <span class="dark">calm</span>
          <span class="light">and</span>
          <span class="light">pause.</span>
        </h2>
      </section>
    </div>

  </main>
</body>
</html>
```